Postcard Design

We are an upscale, full service real estate boutique based in Mt. Pleasant, SC. We will be having a Grand Opening of our beautiful, new office complete with high end custom home architecture and design. I will attach photos for your review. I would like to come up with a medium postcard to be mailed to clientele of Mt. Pleasant. Home prices between $300,000 - $2.2 million. The customers can call our office for the Grand Opening Listing Promotion or stop by our grand opening. We will have drawings for door prizes that include services at Brambleton Day Spa, Copper Kettle gift certificates, and they can register to win a cruise with a listing presentation. Our Grand Opening will be a couple of different dates, April 7, 2016 and April 21, 2016. I will want an order that lists the 7th and another order that will list the 21. The look should have a very "relaxing, beach" feel, but not Myrtle Beach...should reflect colors of the ocean, like you are on vacation. I will include logos and pics for your review. Thank you!

```html
<!DOCTYPE html>
<html lang="en">
<head>
<meta charset="utf-8">
<title>Harborline Real Estate – Grand Opening Postcard</title>
<link rel="stylesheet" href="https://fonts.googleapis.com/css2?family=Montserrat:wght@400;500;600;700&display=swap">
<style>
  :root {
    --frame: #000000;
    --ocean: #0a7bc1;
    --ocean-light: #2aa8df;
    --ocean-glass: rgba(10, 123, 193, 0.88);
    --brand: #1a93c6;
    --band: rgba(255, 255, 255, 0.86);
    --logo-panel: rgba(255, 255, 255, 0.82);
    --ink: #111111;
    --white: #ffffff;
  }
  * { margin: 0; padding: 0; box-sizing: border-box; }
  html, body {
    width: 1200px;
    height: 790px;
    overflow: hidden;
    background: var(--frame);
    font-family: "Montserrat", Arial, sans-serif;
  }
  .postcard {
    position: absolute;
    left: 17px;
    top: 17px;
    width: 1157px;
    height: 748px;
    overflow: hidden;
    background: var(--ocean);
  }
  .hero-photo {
    position: absolute;
    left: 0; top: 0;
    width: 1157px;
    height: 658px;
    background:
      linear-gradient(90deg, rgba(70,95,50,0.55) 0%, rgba(70,95,50,0) 22%, rgba(70,95,50,0) 72%, rgba(95,105,60,0.6) 100%),
      linear-gradient(180deg, #8fb7dd 0%, #a9c3d6 14%, #8f9aa0 20%, #a7c1d9 34%, #9db8d3 60%, #b8c8cf 80%, #9aa38b 100%);
  }
  .logo-panel {
    position: absolute;
    left: 22px; top: 2px;
    width: 284px; height: 211px;
    background: var(--logo-panel);
    display: flex;
    flex-direction: column;
    align-items: center;
    justify-content: center;
    gap: 12px;
    color: var(--brand);
    font-weight: 600;
  }
  .logo-dot {
    width: 70px; height: 70px;
    border-radius: 50%;
    background: var(--brand);
  }
  .logo-name { font-size: 33px; letter-spacing: 2px; line-height: 1; }
  .logo-sub { font-size: 14px; letter-spacing: 6px; line-height: 1; }
  .price-badge {
    position: absolute;
    left: 923px; top: 2px;
    width: 230px; height: 236px;
  }
  .price-badge svg { position: absolute; inset: 0; }
  .price-badge-text {
    position: absolute;
    inset: 0;
    color: var(--white);
    text-align: center;
    font-weight: 600;
  }
  .price-label {
    position: absolute;
    top: 55px; width: 100%;
    font-size: 18px;
    line-height: 24px;
  }
  .price-range {
    position: absolute;
    top: 105px; width: 100%;
    font-size: 36px;
    line-height: 44px;
    font-weight: 700;
  }
  .event-panel {
    position: absolute;
    left: 0; top: 423px;
    width: 1157px; height: 136px;
    background: var(--ocean-glass);
    color: var(--white);
    text-align: center;
    display: flex;
    flex-direction: column;
    justify-content: center;
    gap: 4px;
  }
  .event-title {
    font-size: 26px;
    font-weight: 700;
    line-height: 34px;
    letter-spacing: 0.5px;
  }
  .event-detail {
    font-size: 16px;
    font-weight: 500;
    line-height: 23px;
  }
  .event-cta { font-weight: 700; }
  .intro-band {
    position: absolute;
    left: 0; top: 559px;
    width: 1157px; height: 99px;
    background: var(--band);
    display: flex;
    align-items: center;
    justify-content: center;
    text-align: center;
    color: var(--ink);
    font-size: 20.5px;
    font-weight: 600;
    line-height: 34px;
    white-space: nowrap;
  }
  .contact-bar {
    position: absolute;
    left: 0; top: 658px;
    width: 1157px; height: 90px;
    background: var(--ocean);
    color: var(--white);
    font-size: 19.5px;
    padding: 13px 0 0 28px;
    line-height: 33px;
  }
  .contact-row { display: flex; align-items: center; white-space: nowrap; }
  .contact-row strong { font-weight: 700; }
  .gap-lg { margin-left: 44px; }
  .gap-md { margin-left: 20px; }
  .phone-icon { margin: 0 12px 0 16px; display: inline-block; vertical-align: middle; }
</style>
</head>
<body>
  <main class="postcard">
    <div class="hero-photo" role="img" aria-label="Photograph of a pale blue two-storey coastal home with grey roof, white trim and storm shutters, framed by pine trees under a blue sky"></div>

    <div class="logo-panel">
      <div class="logo-dot"></div>
      <div class="logo-name">HARBORLINE</div>
      <div class="logo-sub">REAL ESTATE</div>
    </div>

    <div class="price-badge">
      <svg viewBox="-5 -5 240 246" width="230" height="236" aria-hidden="true">
        <g fill="var(--ocean-light)">
          <circle cx="197" cy="118" r="36"/><circle cx="181" cy="168" r="36"/>
          <circle cx="140" cy="199" r="36"/><circle cx="90" cy="199" r="36"/>
          <circle cx="49" cy="168" r="36"/><circle cx="33" cy="118" r="36"/>
          <circle cx="49" cy="68" r="36"/><circle cx="90" cy="37" r="36"/>
          <circle cx="140" cy="37" r="36"/><circle cx="181" cy="68" r="36"/>
          <ellipse cx="115" cy="118" rx="90" ry="92"/>
        </g>
        <g fill="var(--ocean)">
          <circle cx="197" cy="118" r="31"/><circle cx="181" cy="168" r="31"/>
          <circle cx="140" cy="199" r="31"/><circle cx="90" cy="199" r="31"/>
          <circle cx="49" cy="168" r="31"/><circle cx="33" cy="118" r="31"/>
          <circle cx="49" cy="68" r="31"/><circle cx="90" cy="37" r="31"/>
          <circle cx="140" cy="37" r="31"/><circle cx="181" cy="68" r="31"/>
          <ellipse cx="115" cy="118" rx="86" ry="88"/>
        </g>
      </svg>
      <div class="price-badge-text">
        <p class="price-label">HOME PRICES<br>BETWEEN</p>
        <p class="price-range">$300K<br>$2.2 M</p>
      </div>
    </div>

    <section class="event-panel">
      <h1 class="event-title">GRAND OPENING · Thursday, April 7, 2016</h1>
      <p class="event-detail">Door prize drawings: services at Brambleton Day Spa, Copper Kettle gift certificates,<br>and register to win a cruise with a listing presentation.</p>
      <p class="event-detail event-cta">Call our office for the Grand Opening Listing Promotion or stop by and celebrate with us!</p>
    </section>

    <section class="intro-band">
      <p>We are an upscale, full service real estate boutique based in Mt. Pleasant, SC.&nbsp; We will be having a<br>Grand Opening of our beautiful, new office complete with high end custom home architecture and design</p>
    </section>

    <footer class="contact-bar">
      <div class="contact-row">
        <span>4820 Harbor Mist Drive Mt. Pleasant, SC 29464</span>
        <span class="gap-lg"><strong>Phone :</strong> (843) 555-0134</span>
        <svg class="phone-icon" width="20" height="22" viewBox="0 0 20 22" aria-hidden="true">
          <rect x="0" y="0" width="20" height="22" rx="3" fill="var(--white)"/>
          <path d="M6 4 L9 4 L10 8 L8 9.5 Q9.5 13 12 14.5 L13.5 12.5 L17 13.5 L17 17 Q11 18 7.5 13 Q5 9 6 4 Z" fill="var(--ocean)"/>
        </svg>
        <span><strong>Fax:</strong> (843) 555-0156</span>
      </div>
      <div class="contact-row">
        <span><strong>Email :</strong> hello@harborline.com</span>
        <span class="gap-md"><strong>Web:</strong> www.harborline.com</span>
      </div>
    </footer>
  </main>
</body>
</html>
```